Harbourline Optical -Window Poster (Optometrist)

We are an optometry practice and we need a poster for a new store promotion for our window highlighting we now also sell 2 pairs of glasses as a package deal. The size will be 1300mm width x 1900mm height

The artwork will be displayed as a fabric banner in our shop window. We have 7 other banners with different services our business provides. The words needs to standout for passers by and the cars stopped at the traffic lights out front of our business. We already have signs with our logos phone number etc. so we won't need them included in the poster.

It would need to include the following information.

Two pair packages now available*

*Conditions apply

The artwork will be displayed as a fabric banner in our shop window. We have 7 other banners with different services our business provides. The words needs to standout for passers by and the cars stopped at the traffic lights out front of our business. We already have signs with our logos phone number etc. so we won't need them included in the poster. Thank you for your work it's amazing Added Saturday, February 18, 2017

The artwork will be displayed as a fabric banner in our shop window. We have 7 other banners with different services our business provides. The words needs to standout for passers by and the cars stopped at the traffic lights out front of our business. We already have signs with our logos phone number etc. so we won't need them included in the poster. Added Saturday, February 18, 2017

Target Market(s)

Cars driving past and stopped at traffic lights outside our store.

Industry/Entity Type

Optician

Requirements
Must have
• Poster must say:
• Two pair packages now available*
• *Conditions apply

```html
<!DOCTYPE html>
<html lang="en">
<head>
<meta charset="utf-8">
<title>Harbourline Optical – Two Pair Packages</title>
<link href="https://fonts.googleapis.com/css2?family=Arimo:wght@400&display=swap" rel="stylesheet">
<style>
  :root {
    --paper: #ffffff;
    --promo-red: #f20000;
    --ink: #111111;
    --frame-light: #f1f1f1;
    --frame-dark: #d6d6d6;
  }
  html, body {
    margin: 0;
    padding: 0;
    overflow: hidden;
    background: var(--paper);
  }
  .poster {
    position: relative;
    width: 821px;
    height: 1200px;
    background: var(--paper);
    overflow: hidden;
    font-family: "Arimo", Arial, sans-serif;
  }
  .eyewear-photo {
    position: absolute;
    border-radius: 40px;
    background: radial-gradient(ellipse at center, var(--frame-dark) 0%, var(--frame-light) 60%, var(--paper) 100%);
  }
  .eyewear-photo--top {
    left: 96px;
    top: 107px;
    width: 632px;
    height: 221px;
  }
  .eyewear-photo--bottom {
    left: 66px;
    top: 881px;
    width: 686px;
    height: 193px;
  }
  .headline-line {
    position: absolute;
    left: 0;
    width: 100%;
    margin: 0;
    text-align: center;
    color: var(--promo-red);
    font-weight: 400;
    font-size: 98px;
    line-height: 1;
    letter-spacing: 1px;
    white-space: nowrap;
  }
  .headline-line--one { top: 388px; }
  .headline-line--two { top: 549px; }
  .headline-line--three { top: 710px; word-spacing: 10px; }
  .conditions {
    position: absolute;
    left: 0;
    width: 100%;
    top: 1111px;
    margin: 0;
    text-align: center;
    color: var(--ink);
    font-size: 46px;
    line-height: 1;
    letter-spacing: 1px;
    white-space: nowrap;
  }
</style>
</head>
<body>
  <main class="poster">
    <div class="eyewear-photo eyewear-photo--top" role="img" aria-label="Photo of black round matte eyeglass frames, front view"></div>

    <h1 class="headline">
      <span class="headline-line headline-line--one">TWO pair</span>
      <span class="headline-line headline-line--two">packages</span>
      <span class="headline-line headline-line--three">now available*</span>
    </h1>

    <div class="eyewear-photo eyewear-photo--bottom" role="img" aria-label="Photo of black glossy panto eyeglass frames with folded arms"></div>

    <p class="conditions">*conditions apply</p>
  </main>
</body>
</html>
```